Bref créative
Business Card Design for Speech Therapy
Under The Willow Speech & Language Therapy
Bright & Fun-filled
Dolores Fairweather, M.S. CCC-SLP
Owner/Director
2715 Quillfeather Road, Suite 340
Largo, MD 20774
therapy@underthewillowx.org
www.underthewillowx.org

```html
<!DOCTYPE html>
<html lang="en">
<head>
<meta charset="utf-8">
<title>Under The Willow Speech &amp; Language Therapy – Stationery</title>
<link rel="stylesheet" href="https://fonts.googleapis.com/css2?family=Fredoka:wght@600&family=Open+Sans:wght@400;600&display=swap">
<style>
  :root {
    --bg: #e4e6e8;
    --paper: #ffffff;
    --orange: #f26a21;
    --green: #6cbf4a;
    --ink: #4a4a4a;
    --muted: #8a8a8a;
    --rule: #c9c9c9;
    --shadow: 0 2px 6px rgba(0,0,0,0.18);
  }
  * { box-sizing: border-box; margin: 0; padding: 0; }
  html, body { width: 1200px; height: 614px; overflow: hidden; }
  body {
    background: var(--bg);
    font-family: "Open Sans", Arial, sans-serif;
    color: var(--ink);
    position: relative;
  }
  .piece {
    position: absolute;
    background: var(--paper);
    box-shadow: var(--shadow);
    overflow: hidden;
  }
  .swoosh {
    position: absolute;
    left: 0; bottom: 0;
    width: 100%;
    display: block;
  }
  .brand {
    display: flex;
    flex-direction: column;
    align-items: center;
    line-height: 1;
  }
  .brand-name {
    font-family: "Fredoka", "Arial Rounded MT Bold", sans-serif;
    font-weight: 600;
    color: var(--orange);
    white-space: nowrap;
  }
  .brand-tagline {
    font-family: "Open Sans", Arial, sans-serif;
    font-weight: 600;
    color: var(--green);
    white-space: nowrap;
    margin-top: 3px;
  }

  /* Envelope */
  .envelope { left: 40px; top: 70px; width: 340px; height: 175px; }
  .envelope .brand { position: absolute; left: 20px; top: 18px; align-items: flex-start; }
  .envelope .brand-name { font-size: 17px; }
  .envelope .brand-tagline { font-size: 7px; }
  .envelope .swoosh { height: 34px; }

  /* Business cards */
  .card { width: 260px; height: 150px; border-radius: 8px; }
  .card-front { left: 80px; top: 270px; }
  .card-front .brand { position: absolute; left: 0; right: 0; top: 42px; }
  .card-front .brand-name { font-size: 24px; }
  .card-front .brand-tagline { font-size: 8.5px; }
  .card-front .swoosh { height: 30px; }

  .card-back { left: 80px; top: 440px; }
  .card-back .contact { position: absolute; left: 20px; top: 16px; }
  .card-back .person { font-size: 11px; font-weight: 600; color: var(--orange); }
  .card-back .role { font-size: 8px; color: var(--green); font-weight: 600; margin-bottom: 8px; }
  .card-back .line { font-size: 7.5px; line-height: 1.45; color: var(--ink); }
  .card-back .swoosh { height: 28px; }

  /* Letterhead */
  .letterhead { left: 420px; top: 50px; width: 360px; height: 514px; }
  .letterhead .brand { position: absolute; left: 0; right: 0; top: 24px; }
  .letterhead .brand-name { font-size: 22px; }
  .letterhead .brand-tagline { font-size: 8px; }
  .letterhead .swoosh { height: 46px; }

  /* Intake form */
  .form-sheet { left: 810px; top: 50px; width: 360px; height: 514px; }
  .form-sheet .form-code { position: absolute; right: 22px; top: 14px; font-size: 9px; font-weight: 600; color: var(--ink); }
  .form-table {
    position: absolute; left: 22px; top: 34px; width: 316px;
    border-collapse: collapse; font-size: 6.5px; color: var(--muted);
  }
  .form-table td { border: 1px solid var(--rule); height: 14px; padding: 0 4px; }
  .form-table .label { width: 46px; background: #f4f4f4; }
  .checks { position: absolute; left: 22px; top: 108px; display: flex; gap: 14px; font-size: 6.5px; color: var(--muted); }
  .check { display: flex; align-items: center; gap: 3px; }
  .check-box { width: 7px; height: 7px; border: 1px solid var(--rule); border-radius: 50%; }
  .form-sheet .swoosh { height: 46px; }
</style>
</head>
<body>

  <section class="piece envelope" aria-label="Envelope">
    <div class="brand">
      <span class="brand-name">Under The Willow</span>
      <span class="brand-tagline">Speech &amp; Language Therapy</span>
    </div>
    <svg class="swoosh" viewBox="0 0 340 34" preserveAspectRatio="none" aria-hidden="true">
      <path d="M0 20 Q170 30 340 6" fill="none" stroke="var(--green)" stroke-width="1.5"/>
      <path d="M0 24 Q170 32 340 10 L340 34 L0 34 Z" fill="var(--orange)"/>
    </svg>
  </section>

  <section class="piece card card-front" aria-label="Business card front">
    <div class="brand">
      <span class="brand-name">Under The Willow</span>
      <span class="brand-tagline">Speech &amp; Language Therapy</span>
    </div>
    <svg class="swoosh" viewBox="0 0 260 30" preserveAspectRatio="none" aria-hidden="true">
      <path d="M0 17 Q130 28 260 5" fill="none" stroke="var(--green)" stroke-width="1.5"/>
      <path d="M0 21 Q130 30 260 9 L260 30 L0 30 Z" fill="var(--orange)"/>
    </svg>
  </section>

  <section class="piece card card-back" aria-label="Business card back">
    <div class="contact">
      <p class="person">Dolores Fairweather, M.S. CCC-SLP</p>
      <p class="role">Owner/Director</p>
      <p class="line">2715 Quillfeather Road, Suite 340</p>
      <p class="line">Largo, MD 20774</p>
      <p class="line">Tel (301) 555-0142</p>
      <p class="line">therapy@underthewillowx.org</p>
      <p class="line">www.underthewillowx.org</p>
    </div>
    <svg class="swoosh" viewBox="0 0 260 28" preserveAspectRatio="none" aria-hidden="true">
      <path d="M0 16 Q130 26 260 4" fill="none" stroke="var(--green)" stroke-width="1.5"/>
      <path d="M0 20 Q130 28 260 8 L260 28 L0 28 Z" fill="var(--orange)"/>
    </svg>
  </section>

  <section class="piece letterhead" aria-label="Letterhead">
    <div class="brand">
      <span class="brand-name">Under The Willow</span>
      <span class="brand-tagline">Speech &amp; Language Therapy</span>
    </div>
    <svg class="swoosh" viewBox="0 0 360 46" preserveAspectRatio="none" aria-hidden="true">
      <path d="M0 28 Q180 42 360 8" fill="none" stroke="var(--green)" stroke-width="2"/>
      <path d="M0 33 Q180 46 360 13 L360 46 L0 46 Z" fill="var(--orange)"/>
    </svg>
  </section>

  <section class="piece form-sheet" aria-label="Intake form">
    <p class="form-code">DX</p>
    <table class="form-table">
      <tr><td class="label">Client</td><td></td><td class="label">Date</td><td></td></tr>
      <tr><td class="label">Birth Date</td><td></td><td class="label">Phone</td><td></td></tr>
      <tr><td class="label">Parent</td><td></td><td class="label">School</td><td></td></tr>
      <tr><td class="label">Address</td><td></td><td class="label">Grade</td><td></td></tr>
    </table>
    <div class="checks">
      <span class="check"><span class="check-box"></span>Intake</span>
      <span class="check"><span class="check-box"></span>Re-Eval</span>
      <span class="check"><span class="check-box"></span>Progress Note</span>
      <span class="check"><span class="check-box"></span>Home Plan</span>
      <span class="check"><span class="check-box"></span>Parent Report</span>
    </div>
    <svg class="swoosh" viewBox="0 0 360 46" preserveAspectRatio="none" aria-hidden="true">
      <path d="M0 28 Q180 42 360 8" fill="none" stroke="var(--green)" stroke-width="2"/>
      <path d="M0 33 Q180 46 360 13 L360 46 L0 46 Z" fill="var(--orange)"/>
    </svg>
  </section>

</body>
</html>
```